graphic design for music festival

Need a design for webpage header and facebook a music festival that fits the location.

A logo type header that can overly on header with Coral Tide Sound Gathering in it !

the location is airlie beach whitsundays and it is called the

Coral Tide Sound Gathering
8th/9th/10th November 2013
65 bands over 3 days 16 venues

the bands are like lorna whitfield, velvet magpies, dale hurst etc..

they have started a facebook page called coral tide sound gathering

need a theme/style to use for facebook cover and a header for webpages.
Updates

Reason: still need work and changing to commiting to pay !

ive gone to commit to pay for a design and added 7 days

Target Market(s)

music people who like the artists in question middle aged australians who like music really

Industry/Entity Type

Graphic Design

Requirements
Must have
• header desgin for webpages and facebook

```html
<!DOCTYPE html>
<html lang="en">
<head>
<meta charset="utf-8">
<title>Coral Tide Sound Gathering – Header</title>
<link rel="stylesheet" href="https://fonts.googleapis.com/css2?family=Cinzel:wght@700;900&display=swap">
<style>
  :root {
    --band-top: #e8501a;
    --band-top-deep: #e0430c;
    --band-bottom: #ec7a14;
    --band-bottom-deep: #e25a10;
    --title: #d9561c;
    --glow: #ffffff;
    --ring: #b83a0c;
    --figure: #d8581e;
    --crowd-dark: #241a10;
    --light-gold: #f2c23a;
    --light-red: #e8562a;
    --haze: #f7f3ea;
  }
  html, body {
    margin: 0;
    padding: 0;
    width: 1200px;
    height: 372px;
    overflow: hidden;
    background: #ffffff;
  }
  .header {
    position: relative;
    width: 1200px;
    height: 372px;
    overflow: hidden;
    font-family: "Cinzel", "Times New Roman", serif;
  }
  .stage-photo {
    position: absolute;
    left: 0;
    top: 40px;
    width: 1200px;
    height: 285px;
    background:
      linear-gradient(90deg, rgba(247,243,234,0) 0%, rgba(247,243,234,0) 30%, rgba(247,243,234,0.85) 44%, rgba(247,243,234,0.97) 62%, rgba(247,243,234,0.9) 86%, rgba(247,243,234,0.2) 100%),
      linear-gradient(180deg, rgba(36,26,16,0) 0%, rgba(36,26,16,0) 45%, rgba(36,26,16,0.75) 72%, rgba(36,26,16,0.95) 100%),
      radial-gradient(ellipse 120px 160px at 300px 40px, rgba(255,245,220,0.9) 0%, rgba(255,245,220,0) 100%),
      radial-gradient(ellipse 160px 200px at 200px 60px, rgba(232,86,42,0.85) 0%, rgba(232,86,42,0) 100%),
      radial-gradient(ellipse 200px 220px at 30px 70px, rgba(242,194,58,0.95) 0%, rgba(242,194,58,0) 100%),
      radial-gradient(ellipse 180px 220px at 1170px 60px, rgba(230,200,110,0.9) 0%, rgba(230,200,110,0) 100%),
      linear-gradient(90deg, #b8901e 0%, #c46a22 30%, #e8c88a 55%, #f0dca8 100%);
  }
  .band {
    position: absolute;
    left: 0;
    width: 100%;
  }
  .band--top {
    top: 0;
    height: 46px;
    background: linear-gradient(180deg, var(--band-top-deep) 0%, var(--band-top) 70%, #ef6a34 100%);
  }
  .band--bottom {
    bottom: 0;
    height: 54px;
    background: linear-gradient(180deg, var(--band-bottom-deep) 0%, var(--band-bottom) 55%, #f0921a 100%);
  }
  .jumper-art {
    position: absolute;
    left: 414px;
    top: 84px;
    width: 96px;
    height: 140px;
    border-radius: 46% 46% 30% 30%;
    background: linear-gradient(180deg, var(--figure) 0%, #c94e18 100%);
    opacity: 0.95;
  }
  .inset-photo {
    position: absolute;
    left: 18px;
    top: 172px;
    width: 170px;
    height: 170px;
    border-radius: 50%;
    border: 7px solid var(--ring);
    box-sizing: border-box;
    background:
      linear-gradient(180deg, rgba(0,0,0,0) 0%, rgba(0,0,0,0) 58%, #0c0c0c 80%, #000 100%),
      radial-gradient(circle at 48% 38%, #ffffff 0%, #dcdcdc 22%, #7a7a7a 50%, #2a2a2a 80%);
    box-shadow: 0 0 0 2px #f3a05a;
  }
  .title {
    position: absolute;
    left: 460px;
    width: 680px;
    margin: 0;
    text-align: center;
    color: var(--title);
    text-shadow: 0 0 3px var(--glow), 0 0 6px var(--glow), 0 0 10px var(--glow);
    line-height: 1;
    font-weight: 700;
    white-space: nowrap;
  }
  .title__name { top: 84px; left: 458px; font-size: 60px; font-weight: 900; }
  .title__kind { top: 153px; left: 478px; font-size: 34px; }
  .title__dates { top: 195px; left: 448px; font-size: 35px; }
  .title__dates sup { font-size: 19px; vertical-align: 14px; }
  .title__count { top: 238px; left: 468px; font-size: 37px; }
</style>
</head>
<body>
  <header class="header">
    <div class="stage-photo" role="img" aria-label="Concert crowd with raised hands under warm gold and red stage lights, fading to light haze on the right"></div>
    <div class="band band--top"></div>
    <div class="band band--bottom"></div>
    <div class="jumper-art" role="img" aria-label="Orange silhouette of a child jumping with arms raised"></div>
    <div class="inset-photo" role="img" aria-label="Round photo of a performer on a bright stage above a dark crowd"></div>

    <h1 class="title title__name">CORAL TIDE</h1>
    <p class="title title__kind">SOUND GATHERING</p>
    <p class="title title__dates">8<sup>TH</sup>/9<sup>TH</sup>/10<sup>TH</sup> NOVEMBER 2013</p>
    <p class="title title__count">65 BANDS OVER 3 DAYS 16 VENUES</p>
  </header>
</body>
</html>
```